Brochure design for Veltrisa

Create a bi-fold A5 size brochure. I have attached our logo and the written content to be included in the brochure. So the brochure will have a total of 4 pages (front page, inner two pages, back page). End source files need to include final printable brochure as well as editable files.

```html
<!DOCTYPE html>
<html lang="en">
<head>
<meta charset="utf-8">
<title>Veltrisa bi-fold brochure</title>
<link href="https://fonts.googleapis.com/css2?family=Comfortaa:wght@300;400;700&display=swap" rel="stylesheet">
<style>
  :root {
    --backdrop: #66666a;
    --paper: #ffffff;
    --paper-shade: #e9e9ec;
    --blue: #3c5ea8;
    --green: #7ab641;
    --ink: #3a3a3f;
    --ink-soft: #5a5a60;
    --ref-bar: #d9d9dc;
    --note-grey: #8f8f93;
  }
  html, body { margin: 0; width: 1200px; height: 1200px; overflow: hidden; background: var(--backdrop); }
  .stage { position: relative; width: 1500px; height: 1500px; transform: scale(0.8); transform-origin: 0 0; font-family: 'Comfortaa', sans-serif; color: var(--ink); }
  .spread { position: absolute; left: 155px; width: 1191px; height: 596px; background: var(--paper); box-shadow: 0 2px 8px rgba(0,0,0,.25); overflow: hidden; }
  .spread--outer { top: 136px; }
  .spread--inner { top: 769px; background: linear-gradient(90deg, #f2f2f4 0%, #fff 30%, #fff 48%, var(--paper-shade) 50%, #fff 54%, #fff 100%); }
  .shapes { position: absolute; left: 0; top: 0; }
  .abs { position: absolute; }

  .back-contacts { left: 0; width: 596px; top: 506px; text-align: center; color: #eef3f0; font-size: 11.5px; line-height: 14.5px; letter-spacing: .4px; font-weight: 300; }
  .back-contacts strong { font-weight: 700; color: #fff; }

  .cover-headline { left: 623px; top: 84px; color: #fff; font-size: 19px; line-height: 22.8px; letter-spacing: .8px; text-transform: uppercase; font-weight: 300; }
  .cover-headline b { font-weight: 700; }
  .cover-sub { left: 623px; top: 294px; color: #dfe6f4; font-size: 13px; line-height: 16.8px; letter-spacing: .5px; text-transform: uppercase; font-weight: 300; }
  .brand { left: 940px; top: 40px; display: flex; align-items: center; gap: 8px; }
  .brand-mark { width: 22px; height: 22px; border-radius: 50%; background: var(--blue); }
  .brand-name { font-size: 30px; font-weight: 700; color: var(--blue); letter-spacing: -.5px; }
  .brand-tag { left: 972px; top: 72px; font-size: 7.5px; color: var(--blue); font-weight: 700; }
  .cover-tagline { left: 777px; top: 509px; font-size: 19px; line-height: 22.5px; color: var(--ink-soft); letter-spacing: .6px; font-weight: 300; }
  .cover-tagline b { color: var(--ink); font-weight: 700; }

  .section { position: absolute; width: 488px; }
  .section-title { font-size: 14.5px; font-weight: 400; color: var(--blue); letter-spacing: .5px; margin: 0 0 10px; padding-bottom: 5px; border-bottom: 1px solid var(--blue); }
  .section-title b { color: var(--green); font-weight: 700; }
  .section p { margin: 0; font-size: 7.6px; line-height: 10.8px; text-align: justify; color: var(--ink-soft); }

  .contact-band { left: 752px; top: 240px; width: 283px; height: 55px; }
  .contact-band p { position: absolute; left: 0; top: 10px; width: 100%; margin: 0; text-align: center; color: #fff; font-size: 7.8px; line-height: 10.8px; }
  .note { left: 650px; top: 304px; width: 487px; text-align: center; color: #fff; font-size: 7.8px; line-height: 10.8px; }
  .refs { left: 650px; top: 351px; width: 487px; margin: 0; padding: 0; list-style: none; }
  .refs li { display: flex; align-items: stretch; margin-bottom: 2px; background: var(--ref-bar); font-size: 6px; line-height: 7.6px; color: var(--ink); min-height: 13px; }
  .refs .num { width: 16px; flex: none; background: var(--blue); color: #fff; display: flex; align-items: center; justify-content: center; margin-right: 6px; }
  .refs .txt { padding: 2.5px 4px 2.5px 0; }
</style>
</head>
<body>
<div class="stage">

  <section class="spread spread--outer" aria-label="Outer spread: back and front cover">
    <svg class="shapes" width="1191" height="596" viewBox="0 0 1191 596">
      <defs>
        <linearGradient id="backGrad" x1="0" y1="0" x2="1" y2="1">
          <stop offset="0" stop-color="#7ab241"/><stop offset=".55" stop-color="#5f9e86"/><stop offset="1" stop-color="#3d62b0"/>
        </linearGradient>
        <linearGradient id="bandGrad" x1="0" y1="1" x2="1" y2="0">
          <stop offset="0" stop-color="#3c5ea8"/><stop offset=".45" stop-color="#3c5ea8"/><stop offset="1" stop-color="#7ab641"/>
        </linearGradient>
        <linearGradient id="photoGrad" x1="0" y1="1" x2="1" y2="0">
          <stop offset="0" stop-color="#cfd9e4"/><stop offset=".35" stop-color="#6f8fb6"/><stop offset=".7" stop-color="#8fc24f"/><stop offset="1" stop-color="#c7e4a2"/>
        </linearGradient>
      </defs>
      <rect x="0" y="0" width="596" height="596" fill="url(#backGrad)"/>
      <rect x="596" y="0" width="595" height="596" fill="#f4f4f6"/>
      <polygon points="596,56 867,56 793,399 596,399" fill="url(#bandGrad)"/>
      <polygon points="596,272 805,272 778,399 596,399" fill="#3a5aa3"/>
      <line x1="884" y1="0" x2="773" y2="540" stroke="#b9b9be" stroke-width="1"/>
      <g role="img" aria-label="Photo of a pipette dispensing green liquid into laboratory test tubes">
        <polygon points="883,126 1191,126 1191,469 777,469" fill="url(#photoGrad)"/>
      </g>
    </svg>
    <div class="abs back-contacts"><strong>Business Contacts:</strong><br>+49 (30) 555 014 230<br>booking@harbourline.com<br>www.harbourline.com</div>
    <div class="abs cover-headline">A <b>Revolution</b><br><b>in Health &amp;</b><br><b>Wellness</b><br>has been<br>brewing<br>– and <b>now</b><br><b>it is here!</b></div>
    <div class="abs cover-sub">Precision health<br>and wellness is<br>tailored to your<br>unique genetic<br>make-up.</div>
    <div class="abs brand"><span class="brand-mark"></span><span class="brand-name">veltrisa</span></div>
    <div class="abs brand-tag">Personalised Health &amp; Wellness</div>
    <div class="abs cover-tagline">We’re <b>helping</b> to build<br>the <b>future of good health</b></div>
  </section>

  <section class="spread spread--inner" aria-label="Inner spread">
    <svg class="shapes" width="1191" height="596" viewBox="0 0 1191 596">
      <defs>
        <linearGradient id="ctaGrad" x1="0" y1="0" x2="1" y2="0">
          <stop offset="0" stop-color="#3c5ea8"/><stop offset=".6" stop-color="#4f78a0"/><stop offset="1" stop-color="#7ab641"/>
        </linearGradient>
      </defs>
      <polygon points="771,240 1016,240 1035,295 752,295" fill="url(#ctaGrad)"/>
      <polygon points="670,295 1116,295 1137,351 650,351" fill="var(--note-grey)"/>
    </svg>

    <div class="section" style="left:53px;top:50px">
      <h2 class="section-title">Precision <b>Health &amp; Wellness</b></h2>
      <p>You are unique. Your healthcare and lifestyle decisions need to be tailored to you. Ever since the human genome was decoded, a plethora of scientific data has revealed everything from disease-causing genes to genetically tailored diets. We all want to live longer and healthier lives, whilst performing at our peak. One size does not fit all and the only way to find out what’s right for you is to unlock your hidden code.</p>
    </div>
    <div class="section" style="left:53px;top:135px">
      <h2 class="section-title">DNA – <b>The Code of Life</b></h2>
      <p>Every individual living organism has a completely unique set of DNA. Your DNA is the chemical blueprint that codes for everything in your body and is found in all of the trillions of cells that you are made of. Collections of DNA are called genes and the complete set of genes in an individual is referred to as their genome. The human genome was first decoded in 2003, taking over 13 years and $2.7 billion to complete. Thanks to exponential advances in technology, veltrisaTM can now unlock your DNA for only a fraction of the time and cost.</p>
    </div>
    <div class="section" style="left:53px;top:231px">
      <h2 class="section-title">Unlock <b>Your Hidden Code</b></h2>
      <p>A whole new world of discovery awaits with the veltrisaTM range of genetic testing services. From unlocking your complete genome with Whole Genome Sequencing (WGS) to just learning about specific aspects of what makes you… you. With veltrisaTM, you can find answers to the questions that can help you to live a healthier, longer and optimal quality of life.</p>
    </div>
    <div class="section" style="left:53px;top:317px">
      <h2 class="section-title">DNA <b>&amp; Disease</b></h2>
      <p>Prevention is better than any cure. Scientific studies have uncovered numerous genes associated with a range of cancers, heart conditions, and other common diseases affecting society today. The range of genetic tests available through veltrisaTM can now identify if these, and other, genes are present in you. This allows you and your physician to potentially prevent, manage, monitor and treat relevant conditions. Furthermore, as the rapid pace of science continues to uncover new genes related to disease, veltrisaTM can quickly update you and your doctor with the latest research and what it means for you*.</p>
    </div>
    <div class="section" style="left:53px;top:425px">
      <h2 class="section-title">DNA <b>&amp; Drugs</b></h2>
      <p>Scientific research has shown that the response rate for many prescribed drugs is as low as 50% and that genetic factors can account for up to 95% of drug-response variability and susceptibility.2-3 In other words, many of the drugs you take in your lifetime will likely be inadequately dosed, leading to potential side effects or no effects at all. With veltrisaTM, you and your doctor can proactively identify appropriate types, and dosages, for a range of prescribed and over-the-counter medications. This includes medications you currently take and any commons future medications you are likely to encounter at some stage in your life. A number of studies have shown that over 74% of people taking a genetic test for medication compatibility learned information that is relevant to them.4-7</p>
    </div>

    <div class="section" style="left:649px;top:50px">
      <h2 class="section-title">DNA <b>&amp; Diet</b></h2>
      <p>Certain foods are thought to inappropriately cause immune reactions in genetically predisposed individuals. This can result in symptoms like fatigue, bloating, bowel disturbances, headaches, migraines, joint aches, eczema or acne8-11. DNA testing can help identify such foods as well as genes associated with the metabolism and absorption of vitamins, minerals and stimulants like coffee. The veltrisaTM range of tests can even help create precision diet and fitness plans based on your genes and goals.</p>
    </div>
    <div class="section" style="left:649px;top:149px">
      <h2 class="section-title">DNA <b>&amp; Descent</b></h2>
      <p>The discipline of genealogy has exploded over recent years with the advent of DNA testing. The veltrisaTM range of tests can help you track and understand your ancestry and paternity tests can help identify an individual’s biological father. Family planning tests can help identify a couple’s risk profile for conceiving children with any of the dozens of known genetic conditions that can affect humans.</p>
    </div>

    <div class="abs contact-band"><p>For more information about veltrisaTM<br>or our products, please talk to your local retailer<br>or email us at <b>enquiries@veltrisa.co</b></p></div>
    <div class="abs note">Please note test availability may differ from region to region and is subject to availability.<br>Please talk to your local retailer for more information.<br>For a list of approved veltrisaTM retailers please visit www.veltrisa.co</div>

    <ol class="abs refs">
      <li><span class="num">01</span><span class="txt">Release notes: Helix Sequencing Alliance completes its reference project. Alliance Bulletin, 2003.</span></li>
      <li><span class="num">02</span><span class="txt">Lund KA, et al. Applied gene–drug review. Northbridge Review of Medicine 4 (2031):12-19.</span></li>
      <li><span class="num">03</span><span class="txt">Moreau P, et al. Quarterly Notes in Gene Science 2032;3:41-58.</span></li>
      <li><span class="num">04</span><span class="txt">Tan R, et al. Harbourline Letters in Diagnostics 2033;7(2):88-94.</span></li>
      <li><span class="num">05</span><span class="txt">Osei W, et al. Meridian Papers in Dosing Practice 2034;12(1):5-11.</span></li>
      <li><span class="num">06</span><span class="txt">Halden N, et al. Coastal Annals of Tailored Care 2034;2(6):30-37.</span></li>
      <li><span class="num">07</span><span class="txt">Varga SL, et al. Meridian Papers in Dosing Practice 2035;13(3):60-66.</span></li>
      <li><span class="num">08</span><span class="txt">Ilves W, et al. Diet trials guided by antibody testing in bowel complaints. Greenfield Gut Digest 9 (2032):14-22.</span></li>
      <li><span class="num">09</span><span class="txt">Brandt N, et al. Trial of an elimination diet for recurring headaches. Open Table Nutrition Notes 5 (2033):71.</span></li>
      <li><span class="num">10</span><span class="txt">Okafor CM, et al. Food reactions linked with headaches in adults. Veldt Allergy Record 8 (2034):40-46.</span></li>
      <li><span class="num">11</span><span class="txt">Lindqvist C, et al. Immune responses in food-linked joint pain. Veldt Allergy Record 9 (2035):18-23.</span></li>
    </ol>
  </section>

</div>
</body>
</html>
```